Dance Card to Provide Contact Info

I'm looking for a double sided business card to provide contact information to perspective dance partners.
One side of the card would have the words: "Yes I would love to Dance" written in an interesting and eye catching way. Below that would be the three categories I'm interested in
>Social >Exhibition >Competition
The other side of the card would include a picture of me with my Name, Phone Number, and Email Address (Dale Penwick, 210-547-2183, dale@twirlmerry.dance)
My target market is middle aged women interested in Country and Western dancing and West Coast Swing dancing. I am NOT particularly interested in Ballroom style.
Here are a few links to the type of dancing I want to do:
http://www.fpqlx.org/
http://www.prairiestepguildnetwork.com/
http://bexarridgepartnerspin.com/
Business
Contact Information for Business Card
Dale Penwick
210-547-2183
dale@twirlmerry.dance

```html
<!DOCTYPE html>
<html lang="en">
<head>
<meta charset="utf-8">
<title>Dale Penwick – Dance Card</title>
<link rel="stylesheet" href="https://fonts.googleapis.com/css2?family=Lato:wght@400;700;900&family=Tinos:ital@0;1&display=swap">
<style>
  :root {
    --canvas: #ebe8e3;
    --red: #e8232a;
    --red-orange: #ef4423;
    --orange: #f37121;
    --orange-light: #f58426;
    --black: #0d0d0d;
    --white: #ffffff;
    --accent-red: #ee2a2e;
    --photo-dark: #2a2523;
    --photo-warm: #c9876a;
  }
  * { box-sizing: border-box; margin: 0; padding: 0; }
  html, body {
    width: 1200px;
    height: 900px;
    overflow: hidden;
    background: var(--canvas);
  }
  .canvas {
    position: relative;
    width: 1200px;
    height: 900px;
  }
  .card {
    position: absolute;
    left: 240px;
    width: 720px;
    height: 411px;
    overflow: hidden;
    box-shadow: 0 10px 24px rgba(0,0,0,0.22);
  }
  .card--front { top: 24px; }
  .card--back { top: 465px; }

  /* Front side */
  .front-bg {
    position: absolute;
    inset: 0;
    background: linear-gradient(135deg, var(--red) 0%, var(--red-orange) 45%, var(--orange) 100%);
  }
  .front-curve {
    position: absolute;
    inset: 0;
    width: 100%;
    height: 100%;
  }
  .portrait {
    position: absolute;
    left: 30px;
    bottom: 0;
    width: 400px;
    height: 265px;
    border-radius: 130px 130px 0 0;
    background: linear-gradient(180deg, var(--photo-warm) 0%, #8b5e4c 40%, var(--photo-dark) 75%);
  }
  .contact {
    position: absolute;
    left: 470px;
    top: 128px;
    width: 235px;
    color: var(--white);
    font-family: "Lato", sans-serif;
  }
  .contact__name {
    font-weight: 900;
    font-size: 26px;
    letter-spacing: 0.3px;
    line-height: 1;
    text-transform: uppercase;
    white-space: nowrap;
  }
  .contact__role {
    margin-top: 5px;
    font-weight: 700;
    font-size: 13px;
    letter-spacing: 0.6px;
    color: var(--accent-red);
    text-transform: uppercase;
  }
  .contact__line {
    display: flex;
    align-items: center;
    gap: 9px;
    margin-top: 10px;
    font-size: 16px;
    font-weight: 400;
    white-space: nowrap;
  }
  .contact__role + .contact__line { margin-top: 14px; }
  .contact__icon {
    width: 16px;
    height: 16px;
    flex: none;
    background: var(--accent-red);
    border-radius: 2px;
    display: flex;
    align-items: center;
    justify-content: center;
  }

  /* Back side */
  .card--back {
    background: linear-gradient(160deg, var(--orange-light) 0%, var(--orange) 45%, var(--red-orange) 100%);
    display: flex;
    flex-direction: column;
    align-items: center;
    justify-content: center;
    color: var(--white);
  }
  .tagline {
    font-family: "Tinos", serif;
    text-align: center;
    line-height: 1;
    text-shadow: 0 2px 6px rgba(120, 30, 0, 0.35);
  }
  .tagline__yes {
    display: block;
    font-size: 46px;
    font-style: italic;
  }
  .tagline__middle {
    display: block;
    font-size: 42px;
    margin-top: 6px;
  }
  .tagline__dance {
    display: block;
    font-size: 84px;
    font-style: italic;
    font-weight: 700;
    letter-spacing: 1px;
    margin-top: 4px;
  }
  .tagline__rule {
    width: 260px;
    height: 2px;
    margin: 18px 0 14px;
    background: var(--white);
    opacity: 0.85;
  }
  .categories {
    display: flex;
    gap: 22px;
    list-style: none;
    font-family: "Lato", sans-serif;
    font-weight: 700;
    font-size: 17px;
    letter-spacing: 2px;
    text-transform: uppercase;
  }
  .categories__item {
    display: flex;
    align-items: center;
    gap: 8px;
  }
  .categories__item::before {
    content: "";
    width: 0;
    height: 0;
    border-left: 7px solid var(--white);
    border-top: 5px solid transparent;
    border-bottom: 5px solid transparent;
  }
</style>
</head>
<body>
<main class="canvas">

  <section class="card card--front" aria-label="Card front">
    <div class="front-bg"></div>
    <svg class="front-curve" viewBox="0 0 720 411" preserveAspectRatio="none" aria-hidden="true">
      <path d="M720 0 L390 0 C300 45 258 170 262 411 L720 411 Z" fill="var(--white)"/>
      <path d="M720 0 L432 0 C338 50 296 175 300 411 L720 411 Z" fill="var(--black)"/>
    </svg>
    <div class="portrait" role="img" aria-label="Portrait photo of Dale Penwick, smiling, in a black shirt"></div>
    <div class="contact">
      <h1 class="contact__name">Dale Penwick</h1>
      <p class="contact__role">Dancing Teacher</p>
      <p class="contact__line">
        <span class="contact__icon">
          <svg width="10" height="10" viewBox="0 0 24 24" aria-hidden="true"><path fill="#fff" d="M6.6 10.8a15.1 15.1 0 0 0 6.6 6.6l2.2-2.2a1 1 0 0 1 1-.25 11.4 11.4 0 0 0 3.6.57 1 1 0 0 1 1 1V20a1 1 0 0 1-1 1A17 17 0 0 1 3 4a1 1 0 0 1 1-1h3.5a1 1 0 0 1 1 1c0 1.25.2 2.45.57 3.57a1 1 0 0 1-.25 1z"/></svg>
        </span>
        210-547-2183
      </p>
      <p class="contact__line">
        <span class="contact__icon">
          <svg width="10" height="10" viewBox="0 0 24 24" aria-hidden="true"><path fill="#fff" d="M2 5h20v14H2z M2 5l10 8 10-8" stroke="#ee2a2e" stroke-width="1.5"/></svg>
        </span>
        dale@twirlmerry.dance
      </p>
    </div>
  </section>

  <section class="card card--back" aria-label="Card back">
    <p class="tagline">
      <span class="tagline__yes">Yes</span>
      <span class="tagline__middle">I would love to</span>
      <span class="tagline__dance">Dance</span>
    </p>
    <div class="tagline__rule"></div>
    <ul class="categories">
      <li class="categories__item">Social</li>
      <li class="categories__item">Exhibition</li>
      <li class="categories__item">Competition</li>
    </ul>
  </section>

</main>
</body>
</html>
```